Flyer für Mobile Massage am Arbeitsplatz
Zielgruppe
Der Flyer richtet sich an Geschäftsleitungen, Firmenvorstände, Betriebsräte.
Ich werde den Flyer sowohl persönlich überreichen, als auch postalisch verschicken.
Aufgabenstellung
Es geht um einen Flyer, DIN lang, Hochformat, beidseitig bedruckt.

```html
<!DOCTYPE html>
<html lang="de">
<head>
<meta charset="utf-8">
<title>Mobile Massage am Arbeitsplatz – Flyer</title>
<link href="https://fonts.googleapis.com/css2?family=Cormorant+Garamond:ital,wght@0,500;1,500&family=Open+Sans:wght@300;400;600&display=swap" rel="stylesheet">
<style>
  :root {
    --bg: #e6e1d9;
    --paper: #ffffff;
    --green: #1f5a4c;
    --green-band: #2a5f52;
    --brown: #9b7a68;
    --brown-box: #a98f80;
    --text-grey: #8c8c8c;
    --photo-warm: #b89a86;
    --photo-deep: #6f5a4e;
  }
  * { margin: 0; padding: 0; box-sizing: border-box; }
  html, body { width: 1200px; height: 857px; overflow: hidden; }
  body { background: var(--bg); position: relative; font-family: "Open Sans", sans-serif; }

  .page {
    position: absolute; top: 21px; width: 389px; height: 816px;
    background: var(--paper);
    box-shadow: 0 2px 8px rgba(0,0,0,.18);
  }
  .page--front { left: 202px; }
  .page--back { left: 620px; width: 379px; }

  .emblem {
    position: absolute; top: 18px; width: 104px; height: 80px;
    border-radius: 50% 50% 45% 45%;
    background: radial-gradient(ellipse at 50% 60%, #5e9a88 0%, #2f6a5b 60%, rgba(47,106,91,0) 72%);
  }
  .page--front .emblem { left: 256px; }
  .page--back .emblem { left: 256px; }

  .headline { position: absolute; left: 14px; top: 50px; font-family: "Cormorant Garamond", serif; font-weight: 500; line-height: 1.1; }
  .headline__main { display: block; font-size: 37px; color: var(--brown); }
  .headline__sub { display: block; font-size: 37px; color: var(--green); }

  .band { position: absolute; left: 0; background: var(--green-band); color: #fff; font-size: 15px; line-height: 22px; padding-left: 12px; }
  .band--phone { top: 160px; width: 172px; }
  .band--web { top: 194px; width: 389px; font-size: 15.5px; }

  .photo { position: absolute; }
  .photo--chair { left: 3px; top: 250px; width: 186px; height: 264px; background: linear-gradient(160deg, #d9bfa8, var(--photo-warm) 60%, #8a735f); }
  .photo--shoulder { left: 195px; top: 250px; width: 189px; height: 264px; background: linear-gradient(200deg, #cdb7a6, var(--photo-deep) 70%, #3e3532); }
  .photo--stretch { left: 3px; top: 521px; width: 381px; height: 288px; background: linear-gradient(180deg, #d8c2ad, #b79a84 55%, #8a705e); }

  .tagline { position: absolute; left: 27px; top: 90px; font-family: "Cormorant Garamond", serif; font-style: italic; font-size: 22px; color: var(--green); }

  .copy { position: absolute; left: 27px; width: 333px; font-size: 11.3px; line-height: 14.2px; font-weight: 300; color: var(--text-grey); text-align: justify; }
  .copy--intro { top: 144px; }
  .copy--intro p + p { text-indent: 14px; }
  .copy strong { font-weight: 600; color: var(--green); }
  .copy--tax { top: 372px; color: var(--green); font-weight: 400; }

  .price-box { position: absolute; left: 17px; top: 482px; width: 333px; height: 89px; background: var(--brown-box); color: #fff; padding: 10px 12px; font-size: 12.5px; line-height: 16px; }
  .price-box__title { font-weight: 600; margin-bottom: 2px; }
  .price-box__note { font-size: 9.5px; }

  .photo--duo { left: 160px; top: 430px; width: 205px; height: 372px; border-radius: 40% 40% 10% 10%;
    background: linear-gradient(180deg, rgba(200,190,180,.0), #9fa7b5 25%, #5f7189 60%, #2e8b7a 85%, #2a2a2a); }
</style>
</head>
<body>

<section class="page page--front">
  <div class="emblem" role="img" aria-label="Seerosenblüte als Zierbild"></div>
  <h1 class="headline">
    <span class="headline__main">Mobile Massage</span>
    <span class="headline__sub">am Arbeitsplatz</span>
  </h1>
  <div class="band band--phone">Tel.: 030 – 40918273</div>
  <div class="band band--web">www.massage-im-buero-havelland.de</div>
  <div class="photo photo--chair" role="img" aria-label="Foto: Massage auf dem Massagestuhl im Büro"></div>
  <div class="photo photo--shoulder" role="img" aria-label="Foto: Schultermassage an einer sitzenden Person"></div>
  <div class="photo photo--stretch" role="img" aria-label="Foto: Dehnung der Arme auf dem Massagestuhl"></div>
</section>

<section class="page page--back">
  <div class="emblem" role="img" aria-label="Seerosenblüte als Zierbild"></div>
  <p class="tagline">einfach mal entspannen …</p>
  <div class="copy copy--intro">
    <p>In unseren Massagen am Arbeitsplatz lassen wir Elemente aus der <strong>Shiatsu – Energiemassage</strong> und den <strong>Joint Release – Gelenklockerungen</strong> zusammenfließen. Auf diese Weise eröffnen wir einen Raum für spürbare Entspannung mitten im Arbeitsalltag.</p>
    <p>Die Massagen befreien aus berufsbedingten Zwangshaltungen, wirken stresslindernd und stimmungshebend im team, fokussieren auf die Problemzonen im Büro: Rücken, Nacken, Schulter und Maushand und sind ein Baustein im innerbetrieblichen Gesundheitsmanagement.</p>
  </div>
  <p class="copy copy--tax">Die Kosten können, sofern vom Arbeitgeber getragen, nach §3 Nr.34 EstG von der Steuer abgesetzt werden.</p>
  <div class="price-box">
    <p class="price-box__title">Preise:</p>
    <p>20 Minuten : 16 Euro</p>
    <p>inklusive Anfahrt</p>
    <p class="price-box__note">buchbar ab 4 Personen</p>
  </div>
  <div class="photo photo--duo" role="img" aria-label="Foto: Masseur und Klient auf dem Massagestuhl"></div>
</section>

</body>
</html>
```